Banner poster with different motifs

I'm looking for 5 banners and posters in A1 format in the same design, or the similarity must be recognizable...
Kept quite simple with different titles.

1 ballet
2 Contemporary Dance
3 high heels
4 Salsa & Bachata & Zouk
5 Hip Hop

Modern bright colors
it is for the entrance so that the students see here is a dance school

The text may also be included in the image
The photos are for guidance only; some are our own, some are purchased. However, we are permitted to use them, including our logo, of course.

```html
<!DOCTYPE html>
<html lang="en">
<head>
<meta charset="utf-8">
<title>Solvera Dance Center Frankfurt – Hip Hop</title>
<link rel="stylesheet" href="https://fonts.googleapis.com/css2?family=Arimo:wght@400;700&family=Roboto:wght@400;700&display=swap">
<style>
  :root {
    --sky-blue: #5271ff;
    --sun-orange: #febe5a;
    --white: #ffffff;
    --shadow-blue: #3a4fbf;
    --photo-dark: #2b2a3a;
    --photo-denim: #4a6d9c;
    --photo-gold: #e8b52c;
  }
  html, body {
    margin: 0;
    padding: 0;
    width: 1200px;
    height: 847px;
    overflow: hidden;
    background: var(--sky-blue);
  }
  .poster {
    display: block;
    width: 1200px;
    height: 847px;
  }
  .backdrop { fill: var(--sky-blue); }
  .dot { fill: var(--sun-orange); }
  .brand-ring { fill: none; stroke: var(--white); stroke-width: 1.5; }
  .brand-name {
    font-family: "Arimo", Arial, sans-serif;
    font-weight: 400;
    font-size: 28px;
    letter-spacing: 2px;
    fill: var(--white);
  }
  .brand-tagline {
    font-family: "Arimo", Arial, sans-serif;
    font-size: 8.5px;
    letter-spacing: 2.4px;
    fill: var(--white);
  }
  .headline {
    font-family: "Arimo", Arial, sans-serif;
    font-weight: 400;
    font-size: 167px;
    fill: var(--white);
  }
  .headline-shadow { fill: var(--shadow-blue); opacity: 0.55; }
  .class-list {
    font-family: "Roboto", Arial, sans-serif;
    font-weight: 700;
    font-size: 19px;
    fill: var(--white);
  }
  .footer-line {
    font-family: "Arimo", Arial, sans-serif;
    font-size: 15px;
    fill: var(--white);
  }
</style>
</head>
<body>
<svg class="poster" viewBox="0 0 1200 847" xmlns="http://www.w3.org/2000/svg">
  <defs>
    <linearGradient id="dancers-tone" x1="0" y1="0" x2="0" y2="1">
      <stop offset="0" stop-color="var(--photo-gold)"/>
      <stop offset="0.35" stop-color="var(--photo-dark)"/>
      <stop offset="0.7" stop-color="var(--photo-denim)"/>
      <stop offset="1" stop-color="var(--photo-denim)"/>
    </linearGradient>
  </defs>

  <rect class="backdrop" x="0" y="0" width="1200" height="847"/>

  <!-- decorative dots -->
  <circle class="dot" cx="146" cy="146" r="35"/>
  <circle class="dot" cx="363" cy="427" r="260"/>
  <circle class="dot" cx="777" cy="230" r="62"/>
  <circle class="dot" cx="680" cy="674" r="81"/>
  <circle class="dot" cx="146" cy="705" r="50"/>

  <!-- dancers photo area -->
  <rect class="dancers-photo" role="img" aria-label="Photo of two young hip hop dancers in caps, varsity jackets and jeans striking a pose"
        x="100" y="186" width="448" height="535" rx="40" fill="url(#dancers-tone)" opacity="0.9"/>

  <!-- brand -->
  <g class="brand">
    <circle class="brand-ring" cx="600" cy="59" r="30"/>
    <text class="brand-name" x="600" y="120" text-anchor="middle">SOLVERA</text>
    <text class="brand-tagline" x="600" y="132" text-anchor="middle">DANCE CENTER FRANKFURT</text>
  </g>

  <!-- headline -->
  <g class="headline-group">
    <text class="headline headline-shadow" x="554" y="448" textLength="551" lengthAdjust="spacingAndGlyphs">HIP HOP</text>
    <text class="headline" x="546" y="443" textLength="551" lengthAdjust="spacingAndGlyphs">HIP HOP</text>
  </g>

  <!-- class list -->
  <text class="class-list" x="551" y="493" textLength="482" lengthAdjust="spacingAndGlyphs">BALLET  /  CONTEMPORARY DANCE  /  HIGH HEELS</text>
  <text class="class-list" x="551" y="522" textLength="366" lengthAdjust="spacingAndGlyphs">SALSA &amp; BACHATA &amp; ZOUK  /  HIP HOP</text>

  <!-- footer -->
  <text class="footer-line" x="484" y="762" textLength="632" lengthAdjust="spacing">S O L V E R A   D A N C E   C E N T E R   F R A N K F U R T</text>
</svg>
</body>
</html>
```